7 Reeds Distillery - Bottle Label Design

We are a small craft distillery whose branding needs to incorporate our location on a lake (Lac Vorbelle, Quebec, Canada). A unique aspect of the lake is that people drive floating docks on the lake powered by a small outboard motor (see photos). Back in the 1970’s when Lac Vorbelle was a sparsely populated and difficult-to-access lake in the Gatineau Hills north of Ottawa, the concept of motorized docks was conjured on a lazy afternoon and this single stroke of genius has inadvertently spawned the most exceptional and eccentric lake based community. Throughout the summer, somewhere around four o’clock on any given Friday and Saturday it starts to happen. Docks set sail from their customary landing places - family, friends, snacks and loaded drink coolers in-tow and, as if magnetically drawn, head toward Heron Shoal. Without fail they will come upon a gathering of similar minded floating docks within the vicinity - be guided in with help to moor alongside and within seconds be seamlessly immersed in the festivities. Seldom any longer are these events planned, they have become elemental, a thing organically derived from within the community. This on-going weekly event is the genesis of the strong bond that brings us Seven Reeds Distilling.
Each of the 4 distillery owners have one of these docks so hence the name. We are open to either "7 Reeds" or spelled out as "Seven Reeds" as may be visually appropriate. We are also open to "Distillery" or "Distilling". More detail on the docks themselves, they are 14x16 feet powered by a small outboard motor as shown in the photos. This dock aspect may be difficult to incorporate into the branding but the lake outline is included as an image applicable to include for that local reference aspect. We will be creating very high quality small batch liquors such as vodka, rum, gin and whiskey. Each batch will be triple distilled and perhaps 20 bottles in quantity so very exclusive. We are aiming at a premium feel for the branding. Attached are some bottle label designs that evoke the type of feel we are going for and a photo of the style of blank bottle to design for which is a 750ml Nordic pattern bottle.
In general we are going for more contemporary than traditional, more bold than delicate. If a single label the size desired would be 4 inches wide and 4 inches tall. If a double/split label as in two of the photos the top label would be 3 inches wide and 3 inches tall and the bottom label would be max 4 inches wide and 1.5 inches tall. We are open to the upper label being a "transparent" label to create a printed on bottle effect, perhaps of the brand logo. We are only interested in front label so do not require a back, neck or closure label. The label will require the ability to name the batch style name (example "Tuberov") and then the amplifying information for the type of alcohol (Russian Potato Vodka) in a smaller font. Another example ("Bell Cap" and "London Dry Gin"). Information for bottle size (750ml) and alcohol % (40%) are also to be included. Governmental safety warnings are not required. We are open to use of any colours in the label. The basic label design would be re-used for different types of batches where we would change the style and alcohol name.

Target Market(s)

Up scale premium spirits buyers

Font styles to use
Serif
Sans Serif

Requirements
Must have
• A visual reference to the docks or the lake per the images attached.
Nice to have
• Ideally we can re-use the label design for a different type of Alcohol by changing the alcohol name and style information and maybe the colour of a major element in the label.

```html
<!DOCTYPE html>
<html lang="en">
<head>
<meta charset="utf-8">
<title>Seven Reeds Distillery – Front Labels</title>
<link rel="stylesheet" href="https://fonts.googleapis.com/css2?family=Playfair+Display:wght@400;700&family=Roboto+Condensed:wght@400;700&family=Zilla+Slab:wght@500&family=Yellowtail&display=swap">
<style>
  :root {
    --page: #ffffff;
    --label-black: #141414;
    --label-black-soft: #1e1e1e;
    --copper: #b35a2c;
    --copper-light: #cf7a45;
    --copper-dark: #7e3a1a;
    --paper: #ecebe6;
    --paper-line: #d3c8bd;
    --ink: #2a2a2a;
    --seal: #a8442a;
    --white: #f4f2ee;
  }
  * { box-sizing: border-box; margin: 0; padding: 0; }
  html, body { width: 1119px; height: 1200px; overflow: hidden; background: var(--page); }
  .canvas { position: relative; width: 1119px; height: 1200px; }

  .label {
    position: absolute; top: 300px; width: 520px; height: 600px;
    background: radial-gradient(ellipse at 50% 45%, var(--label-black-soft), var(--label-black) 70%);
  }
  .label--classic { left: 26px; }
  .label--modern { left: 573px; }

  .brand {
    position: absolute; left: 0; right: 0; text-align: center;
    font-family: "Playfair Display", serif; color: var(--copper); white-space: nowrap;
  }
  .label--classic .brand { top: 46px; font-weight: 700; font-size: 88px; line-height: 84px; letter-spacing: 0; }
  .label--modern .brand { top: 100px; font-weight: 400; font-size: 108px; line-height: 112px; }

  .brand-script {
    position: absolute; left: 0; right: 0; top: 216px; text-align: center;
    font-family: "Yellowtail", cursive; font-size: 50px; line-height: 60px; color: var(--white);
  }

  .brand-mark {
    position: absolute; left: 220px; top: 285px; width: 80px; height: 80px; border-radius: 50%;
    background: radial-gradient(circle at 40% 35%, var(--copper-light), var(--copper) 55%, var(--copper-dark));
  }

  .info {
    position: absolute; left: 36px; top: 376px; width: 448px; height: 192px;
  }
  .info-table {
    display: grid; grid-template-columns: 188px 188px 72px; grid-template-rows: 36px 38px 46px;
    background: var(--paper); height: 120px;
  }
  .cell {
    display: flex; align-items: center; padding: 0 13px;
    border-bottom: 1px solid var(--paper-line); font-family: "Playfair Display", serif;
    font-size: 11.5px; color: var(--ink); white-space: nowrap;
  }
  .cell--right { border-left: 1px solid var(--paper-line); }
  .cell--last { border-bottom: none; }
  .cell .key { color: var(--copper); margin-right: 3px; }
  .slab { font-family: "Zilla Slab", serif; font-weight: 500; color: var(--copper); font-size: 12px; }
  .alcohol { font-size: 21px; color: var(--ink); }
  .alcohol .key { font-size: 21px; }
  .alc-vol .key { font-size: 10.5px; letter-spacing: 0.5px; }
  .alc-vol .value { font-family: "Roboto Condensed", sans-serif; font-size: 16px; }
  .alc-vol .e-mark { font-family: "Playfair Display", serif; color: var(--copper); font-size: 24px; margin-left: 8px; }
  .seal-cell { grid-column: 3; grid-row: 1 / span 3; display: flex; align-items: center; justify-content: center; }
  .seal { width: 60px; height: 60px; border-radius: 50%; background: radial-gradient(circle at 40% 35%, #c45a3c, var(--seal) 60%, #7a2c1a); }

  .origin {
    position: relative; height: 72px; padding: 8px 14px;
    background: linear-gradient(90deg, var(--copper-dark), var(--copper) 45%, var(--copper-dark));
    color: var(--white); font-family: "Roboto Condensed", sans-serif;
  }
  .origin-intro { font-size: 11px; line-height: 13px; }
  .origin-place {
    font-weight: 700; font-size: 14px; line-height: 18px; display: inline-block;
    border-bottom: 1px solid var(--white); padding-bottom: 2px; margin-bottom: 3px;
  }
  .origin-notes { font-size: 10.5px; letter-spacing: 0.8px; }
  .origin-art {
    position: absolute; right: 10px; top: 10px; width: 180px; height: 52px;
    background: linear-gradient(90deg, rgba(40,18,8,0.15), rgba(40,18,8,0.5));
  }
</style>
</head>
<body>
<main class="canvas">

  <section class="label label--classic" aria-label="Front label, stacked wordmark">
    <h1 class="brand">SEVEN<br>REEDS</h1>
    <p class="brand-script">Distillery</p>
    <div class="brand-mark"></div>
    <div class="info">
      <div class="info-table">
        <div class="cell">RUSSIAN POTATO VODKA</div>
        <div class="cell cell--right slab">Small Batch | Handcrafted</div>
        <div class="cell"><span class="key">Distillation Date :</span> 24/06/1996</div>
        <div class="cell cell--right"><span class="key">Bottled Date :</span> 15/01/2018</div>
        <div class="cell cell--last alcohol"><span class="key">ALCOHOL :</span>&nbsp;40%</div>
        <div class="cell cell--right cell--last alc-vol"><span class="key">ALC./VOL :</span>&nbsp;<span class="value">40% | 750ml</span><span class="e-mark">e</span></div>
        <div class="seal-cell"><div class="seal"></div></div>
      </div>
      <div class="origin">
        <p class="origin-intro">Distilled, Matured &amp; Bottled In</p>
        <p class="origin-place">LAC VORBELLE, QUEBEC, CANADA</p>
        <p class="origin-notes">NON CHILL FILTERED • NATURAL COLOUR</p>
        <div class="origin-art" role="img" aria-label="Owner's signature beside a silhouette outline of Lac Vorbelle"></div>
      </div>
    </div>
  </section>

  <section class="label label--modern" aria-label="Front label, numeral wordmark">
    <h1 class="brand">7 Reeds</h1>
    <p class="brand-script">Distillery</p>
    <div class="brand-mark"></div>
    <div class="info">
      <div class="info-table">
        <div class="cell">RUSSIAN POTATO VODKA</div>
        <div class="cell cell--right slab">Small Batch | Handcrafted</div>
        <div class="cell"><span class="key">Distillation Date :</span> 24/06/1996</div>
        <div class="cell cell--right"><span class="key">Bottled Date :</span> 15/01/2018</div>
        <div class="cell cell--last alcohol"><span class="key">ALCOHOL :</span>&nbsp;40%</div>
        <div class="cell cell--right cell--last alc-vol"><span class="key">ALC./VOL :</span>&nbsp;<span class="value">40% | 750ml</span><span class="e-mark">e</span></div>
        <div class="seal-cell"><div class="seal"></div></div>
      </div>
      <div class="origin">
        <p class="origin-intro">Distilled, Matured &amp; Bottled In</p>
        <p class="origin-place">LAC VORBELLE, QUEBEC, CANADA</p>
        <p class="origin-notes">NON CHILL FILTERED • NATURAL COLOUR</p>
        <div class="origin-art" role="img" aria-label="Owner's signature beside a silhouette outline of Lac Vorbelle"></div>
      </div>
    </div>
  </section>

</main>
</body>
</html>
```